Quillbrook Cellars Winery… For non-interventionist winemakers, wine-making begins in the

Need a new website for my new winery…previous one lost in divorce to my cheating ex wife…sigh. Calling it Quillbrook Cellars. Want it to look like a wedding sight…calligraphy writing…black and white…with some black roses…want the look of a invitational wedding site…celebratory! We employ a combination of modern techniques and old world traditions, practicing both the cuvee and "field blending" methods, to create a range of distinctive varietals. To ensure flawless berries reach the fermentation process, we hand-sort grapes as soon as we get them into the winery. Our open-top, double-jacketed fermenters allow precise temperature control during "cold soak" periods and primary fermentation -- essential for color, flavor, and tannin extraction. Occasional délestage ("rack & return") aerates the wine. After ratchet basket pressing, we age our wines in French oak barrels for at least 18 months; minimal racking lets wine clarify naturally. Patience, sagacity, gumption, and a balance between both received methods (classic and modern) and ingenuity are foundations for crafting the world-class wines offered by our small, family-run artisanal winery here in the beautiful Walla Walla valley, located beneath the Blue Mountains in eastern Washington

Target Market(s)

Wine drinkers/broken hearts

Industry/Entity Type

Winery

Number of Pages Required

4 page

Font styles to use
Script

Colors

Designer to choose only greyscale colors for use in the design.

Requirements
Must have
• Black roses… From our Walla Walla valley boutique winery here in the Pacific Northwest, we offer a range of premium reds, whites, ice wines, late harvest wines, brandies, grappas, and specialty spirits. We embrace sustainable farming methods on our estate vineyard and source fruit from growers who share our commitment to biodiversity. A great bottle of wine begins with the vine! For our "green wines," we practice innovative eco-friendly techniques, aim for Earth-friendly packaging, and donate a portion of our after-profit proceeds to environmental concerns. Though we appreciate ratings, we're less interested in numbers and more in the approval of our palettes and those of trusted friends, as well as accolades from loyal customers near and far. We handcraft what we hope will become your cult wines, often well into the night, humbled by the calls of barn owls who give our cellar its name.
Nice to have
• Page to list varieties…Wanderpeak Riesling, Moonthistle Sparkling, Dovemarrow Red

```html
<!DOCTYPE html>
<html lang="en">
<head>
<meta charset="utf-8">
<title>Quillbrook Cellars</title>
<link href="https://fonts.googleapis.com/css2?family=Playball&family=Mulish:wght@400;500&display=swap" rel="stylesheet">
<style>
:root{
  --ink:#454b4b;
  --ink-soft:#5b6161;
  --button:#4a504f;
  --paper:#f2f2f3;
  --band:#e0e2e3;
  --rose-dark:#3f4a48;
  --rose-mid:#7d8886;
  --line:#5a605f;
}
*{margin:0;padding:0;box-sizing:border-box}
html,body{width:1200px;height:3417px;overflow:hidden}
body{position:relative;background:var(--paper);color:var(--ink);font-family:'Mulish',sans-serif}
.abs{position:absolute}
.script{font-family:'Playball',cursive;font-weight:400;color:var(--ink)}
.art{position:absolute}
.roses{background:radial-gradient(ellipse at center,var(--rose-dark) 0%,var(--rose-mid) 45%,rgba(242,242,243,0) 72%)}
.brand{font-family:'Playball',cursive;color:var(--ink);font-size:40px;line-height:1;white-space:nowrap}
.nav{display:flex;align-items:stretch}
.nav a{display:flex;flex-direction:column;align-items:center;justify-content:center;gap:6px;text-decoration:none;font-family:'Playball',cursive;color:var(--ink);font-size:22px;padding:0 28px}
.nav a+a{border-left:1.5px solid var(--line)}
.nav svg{width:20px;height:20px;stroke:var(--ink);fill:none;stroke-width:1.4}
.btn{display:inline-flex;align-items:center;justify-content:center;background:var(--button);color:#fff;font-family:'Playball',cursive;font-size:19px;border-radius:23px;text-decoration:none}
.divider{position:absolute;height:2px;width:60px}
.divider::before{content:"";position:absolute;left:0;top:0;width:38px;height:2px;background:var(--ink)}
.divider::after{content:"";position:absolute;left:48px;top:0;width:14px;height:2px;background:var(--ink)}
.body-text{font-size:14.5px;line-height:21.6px;color:var(--ink-soft);text-align:justify}
.wine-band{position:absolute;left:0;top:1457px;width:1200px;height:840px;background:var(--band);clip-path:polygon(0 0,100% 0,100% 803px,0 838px)}
.wine-card{position:absolute;width:300px;text-align:center}
.wine-card .bottle{margin:0 auto;width:90px;height:370px;border-radius:30px 30px 10px 10px;background:linear-gradient(90deg,#1a1a1c,#3d2a33 50%,#151517)}
.wine-card h3{font-family:'Playball',cursive;font-weight:400;font-size:30px;margin-top:42px;color:var(--ink)}
.wine-card p{font-size:14.5px;line-height:20px;color:var(--ink-soft);margin-top:8px}
.footer{position:absolute;left:0;top:2970px;width:1200px;height:447px;background:linear-gradient(#f2f2f3,#e7e8e9 60%,#eeeeef)}
.footer-nav{display:flex;justify-content:center}
.footer-nav a{font-family:'Playball',cursive;font-size:21px;color:var(--ink);text-decoration:none;padding:4px 28px}
.footer-nav a+a{border-left:1.5px solid var(--line)}
</style>
</head>
<body>

<!-- Header -->
<div class="art roses" role="img" aria-label="Black rose and leaf garland along the top edge" style="left:-60px;top:-60px;width:1320px;height:270px;opacity:.85"></div>

<div class="brand abs" style="left:133px;top:208px">Quillbrook Cellars</div>

<nav class="nav abs" style="left:745px;top:172px;height:76px">
  <a href="#"><svg viewBox="0 0 20 20"><path d="M3 10 L10 3 L17 10 M5 8.5 V17 H15 V8.5"/></svg>Home</a>
  <a href="#"><svg viewBox="0 0 20 20"><path d="M6 2 H8 V6 L9 8 V18 H5 V8 L6 6 Z M12 2 H14 V6 L15 8 V18 H11 V8 L12 6 Z"/></svg>Wine</a>
  <a href="#"><svg viewBox="0 0 20 20"><rect x="2.5" y="5" width="15" height="10"/><path d="M2.5 5 L10 11 L17.5 5"/></svg>Contact</a>
</nav>

<!-- Hero -->
<div class="art" role="img" aria-label="Photo of a wedding couple toasting with glasses of white wine in a garden" style="left:560px;top:230px;width:580px;height:630px;background:radial-gradient(ellipse at 55% 50%,#8a8476 0%,#b5b0a6 40%,rgba(242,242,243,0) 72%)"></div>

<h1 class="abs script" style="left:133px;top:380px;font-size:50px;line-height:1.1">Welcome to</h1>
<div class="abs script" style="left:133px;top:440px;font-size:64px;line-height:1.1;white-space:nowrap">Quillbrook Cellars</div>

<p class="abs" style="left:133px;top:553px;width:380px;font-size:16px;line-height:26px;color:var(--ink-soft)">Lorem ipsum dolor sit amet consectetur adip iscing elit, sed do eiusmod tempor incididunt ut labore et dolore magna aliqua.</p>

<a class="btn abs" href="#" style="left:133px;top:665px;width:138px;height:45px">Contact us</a>

<!-- About -->
<div class="art" role="img" aria-label="Photo of a red wine bottle and two glasses on an oak barrel with green and red grapes" style="left:0;top:880px;width:490px;height:577px;background:linear-gradient(160deg,rgba(242,242,243,0) 10%,#6b4a2b 55%,#8a5e33)"></div>

<h2 class="abs script" style="left:587px;top:872px;font-size:64px;line-height:1.1">About us</h2>
<div class="divider" style="left:590px;top:965px"></div>

<p class="abs body-text" style="left:588px;top:1003px;width:478px">We employ a combination of modern techniques and old world traditions, practicing both the cuvee and "field blending" methods, to create a range of distinctive varietals. To ensure flawless berries reach the fermentation process, we hand-sort grapes as soon as we get them into the winery. Our open-top, double-jacketed fermenters allow precise temperature control during "cold soak" periods and primary fermentation -- essential for color, flavor, and tannin extraction. Occasional délestage ("rack &amp; return") aerates the wine. After ratchet basket pressing, we age our wines in French oak barrels for at least 18 months; minimal racking lets wine clarify naturally. Patience, sagacity, gumption, and a balance between both received methods (classic and modern) and ingenuity are foundations for crafting the world-class wines offered by our small, family-run artisanal winery here in the beautiful Walla Walla valley, located beneath the Blue Mountains in eastern Washington</p>

<a class="btn abs" href="#" style="left:588px;top:1355px;width:139px;height:45px">Read More</a>

<!-- Wine -->
<div class="wine-band"></div>
<div class="art roses" role="img" aria-label="Cluster of black roses with leaves" style="left:775px;top:1350px;width:390px;height:250px"></div>

<h2 class="abs script" style="left:0;width:1200px;text-align:center;top:1508px;font-size:60px;line-height:1.1">Wine</h2>
<div class="divider" style="left:562px;top:1610px"></div>

<div class="wine-card" style="left:103px;top:1683px">
  <div class="bottle" role="img" aria-label="Photo of a bottle of riesling with a pink capsule"></div>
  <h3>Wanderpeak Riesling</h3>
  <p>Lorem ipsum dolor sit amet,<br>consectetur adipiscing.</p>
</div>
<div class="wine-card" style="left:453px;top:1683px">
  <div class="bottle" role="img" aria-label="Photo of a dark bottle of sparkling wine" style="background:linear-gradient(90deg,#121213,#2e2e30 50%,#0f0f10)"></div>
  <h3>Moonthistle Sparkling</h3>
  <p>Lorem ipsum dolor sit amet,<br>consectetur adipiscing.</p>
</div>
<div class="wine-card" style="left:815px;top:1680px">
  <div class="bottle" role="img" aria-label="Photo of a bottle of red wine with a red capsule" style="background:linear-gradient(90deg,#101012,#26262a 50%,#0d0d0f)"></div>
  <h3>Dovemarrow Red</h3>
  <p>Lorem ipsum dolor sit amet,<br>consectetur adipiscing.</p>
</div>

<!-- Distinctive Wines -->
<div class="art roses" role="img" aria-label="Black roses with trailing leaves on the left edge" style="left:-40px;top:2190px;width:325px;height:350px"></div>
<div class="art" role="img" aria-label="Pencil sketch of grape bunches and vine leaves" style="left:950px;top:2260px;width:250px;height:720px;background:linear-gradient(90deg,rgba(242,242,243,0),#d9dadb 50%,#e4e5e6)"></div>

<h2 class="abs script" style="left:135px;top:2402px;font-size:62px;line-height:1.1">Distinctive Wines</h2>
<div class="divider" style="left:137px;top:2505px"></div>

<p class="abs body-text" style="left:135px;top:2548px;width:461px">Black roses… From our Walla Walla valley boutique winery here in the Pacific Northwest, we offer a range of premium reds, whites, ice wines, late harvest wines, brandies, grappas, and specialty spirits. We embrace sustainable farming methods on our estate vineyard and source fruit from growers who share our commitment to biodiversity. A great bottle of wine begins with the vine! For our "green wines," we practice innovative eco-friendly techniques, aim for Earth-friendly packaging, and donate a portion of our after-profit proceeds to environmental concerns. Though we appreciate ratings, we're less interested in numbers and more in the approval of our palettes and those of trusted friends, as well as accolades from loyal customers near and far. We handcraft what we hope will become your cult wines, often well into the night, humbled by the calls of barn owls who give our cellar its name.</p>

<div class="art" role="img" aria-label="Photo of red and white wine bottles with filled glasses, dark and green grapes and a vine leaf" style="left:635px;top:2375px;width:370px;height:505px;background:radial-gradient(ellipse at 50% 55%,#4a2a30 0%,#8a8a4a 45%,rgba(242,242,243,0) 72%)"></div>

<!-- Footer -->
<footer class="footer">
  <div class="brand" style="position:absolute;left:0;width:1200px;text-align:center;top:38px">Quillbrook Cellars</div>
  <nav class="footer-nav" style="position:absolute;left:0;width:1200px;top:140px">
    <a href="#">Home</a><a href="#">Wine</a><a href="#">Contact</a>
  </nav>
  <p style="position:absolute;left:0;width:1200px;top:202px;text-align:center;font-size:13px;color:var(--ink-soft)">Copyright © 2024 All Rights Reserved</p>
</footer>

<div class="art roses" role="img" aria-label="Black rose and leaf garland along the bottom edge" style="left:-60px;top:3225px;width:1320px;height:260px;opacity:.85"></div>

</body>
</html>
```